Create a new cutting edge high-end design for our client who runs a signage company specialising in Marine printing, signage for Crusie ships and signage products, refurbishments for Hotels.

“Elevating Spaces with Precision-crafted Hospitality Signage for Marine & Luxury Hotels”

The design has to be cutting edge design and have a high-end look showing past projects to separate them from their competitors.

Sites they like,
I dont like adding these as it can change a perspective on a design, however, I feel pretty confident that this is something they would appreciate there are various aspects of these they

https://www.tidewellmarine.example/
https://www.velborstig.example/en/
https://www.quillanhartint.example/
https://www.telmora.example/
https://dovapex.example/projects/index.html
https://www.pkv-studio.example/

Assets
Fonts -use the fonts we have set in the design of the logos (see attached assets)
Images and graphics - Feel free to source better stock images and if we need to purchase these let me know, otherwise, there are some images from ships and projects they have already worked on. I know these are not that great.
Attached lost of information in documents, feel free to use this as content or ideas.

Shipyards we have worked with
• Varnoscali (Monfalcone, Italy)
• Varnoscali (Genoa- Sestri Ponente, Italy)
• Ateliers de 'lBorvenne (Saint-Nazaire, France)
• Halstrom Turku (Turku, Finland)
• Halstrom Docken (Papenburg, Germany)
• Halstrom Korvid Docken (Rostock, Germany)

Buildings we have worked on
• Glenvaux Hotel, Monte Carlo
• Pike Hotel – London
• Bay Lodgings – London
• Wexbury Rowhouse Hotel – London
• Tazi – London
• Orla Clinic, Dubai
• Dunmore Rowhouse Hotel
• The Strand Hotel, London

Things that we need to have in the design.
Some things to think about in the design:
InfoGraphic of the print process.
List of logos of clients
How to handle the Video opener stock images
Testimonials,
London phone number, London address.
Videos, London dry docks Crusie ships. Richmond
Network Social links
Contact forms
News Section
Services lead section
How we work Section process
Projects section, needs to be creative and stand out, I Am open to suggestions here.
International map with locations across the world of ports worked at. Hover annotation bubbles expand.
Updates

Need extra days to review

Target Market(s)

Cruise Ships and Hotels

Industry/Entity Type

Marine Signage & Luxury Hotels

Number of Pages Required

2 page

Font styles to use
Other font styles liked:
• see assets for attached fonts.

Requirements
Nice to have
• See list.

```html
<!DOCTYPE html>
<html lang="en">
<head>
<meta charset="utf-8">
<title>Veltro — Marine & Luxury Hotel Signage</title>
<link rel="stylesheet" href="https://fonts.googleapis.com/css2?family=Libre+Baskerville:wght@400;700&family=Montserrat:wght@400;500;600;700&display=swap">
<style>
:root{
  --navy:#0c2a4b;
  --ink:#1d2733;
  --muted:#7a838c;
  --orange:#d06e1f;
  --teal:#1c8db0;
  --teal-line:#3aa3c4;
  --beige:#f8f1ea;
  --ice:#e9f4f8;
  --ice-2:#f3f8fb;
  --footer:#0a1f3b;
  --white:#fff;
  --serif:"Libre Baskerville", Georgia, serif;
  --sans:"Montserrat", Arial, sans-serif;
}
*{box-sizing:border-box;margin:0;padding:0}
html,body{width:1200px;height:5052px;overflow:hidden}
body{position:relative;background:var(--white);font-family:var(--sans);color:var(--ink)}
.abs{position:absolute}
.ph{position:absolute;overflow:hidden}
h2.title{font-family:var(--serif);font-weight:700;font-size:20px;line-height:31px;color:var(--ink)}
.btn{position:absolute;display:flex;align-items:center;justify-content:center;background:var(--orange);color:#fff;font-size:10px;font-weight:600;border-radius:2px}
.body-text{font-size:10px;line-height:17.5px;color:var(--muted)}
/* hero */
.hero{position:absolute;left:0;top:0;width:1200px;height:555px;background:linear-gradient(180deg,#8fa7b3 0%,#b9c3c2 40%,#c9b49a 70%,#9a7a5c 85%,#3b4a55 100%)}
.hero-ship{position:absolute;left:560px;top:80px;width:450px;height:400px;background:radial-gradient(ellipse at 55% 55%,#f3f1ec 0%,#d7d9db 45%,rgba(120,130,140,0) 72%)}
.nav{position:absolute;left:173px;top:33px;width:853px;height:56px;background:#fff;border-radius:3px;display:flex;align-items:center;padding:0 17px}
.logo{font-family:var(--serif);font-size:26px;letter-spacing:7px;color:var(--navy)}
.menu{display:flex;gap:23px;margin-left:85px;font-size:10px;font-weight:600;color:var(--navy)}
.nav-cta{margin-left:auto;border:1px solid var(--teal);color:var(--teal);font-size:10px;font-weight:600;padding:9px 18px;border-radius:2px}
.hero h1{position:absolute;left:173px;top:186px;font-family:var(--serif);font-weight:400;font-size:28px;line-height:46px;color:var(--navy)}
.hero h1 em{font-style:normal;color:var(--orange)}
.brands{position:absolute;left:173px;top:494px;width:853px;display:flex;justify-content:space-between;color:#fff;font-family:var(--serif);font-size:17px;font-weight:700}
/* about */
.about-card{position:absolute;left:173px;top:618px;width:584px;height:362px;background:#fff;box-shadow:0 4px 22px rgba(12,42,75,.09)}
.about-card h2{position:absolute;left:31px;top:34px;font-family:var(--serif);font-size:19px;font-weight:700}
.about-card .body-text{position:absolute;left:31px;top:72px;width:328px}
/* services */
.svc-grid{position:absolute;left:173px;top:1202px;width:853px;height:376px;display:grid;grid-template-columns:repeat(3,1fr);grid-template-rows:1fr 1fr}
.svc{text-align:center;padding-top:28px;border:1.5px dashed transparent}
.svc.framed{border-color:var(--teal-line)}
.svc svg{width:62px;height:62px}
.svc h3{font-family:var(--serif);font-size:12.5px;margin:14px 0 10px}
.svc p{font-size:10px;line-height:16px;color:var(--muted);width:230px;margin:0 auto}
/* how */
.how-list{position:absolute;left:619px;top:1826px;list-style:none}
.how-list li{display:flex;align-items:center;gap:18px;height:44px;font-size:12px;font-weight:500}
.how-list svg{width:30px;height:30px}
/* process */
.process{position:absolute;left:0;top:2059px;width:1200px;height:451px;background:var(--beige)}
.step{position:absolute;width:210px;text-align:center}
.step h4{font-family:var(--serif);font-size:12px;margin-bottom:6px}
.step p{font-size:9.5px;line-height:17px;color:var(--muted)}
.node{position:absolute;width:78px;height:78px;border-radius:50%;background:#fff;display:flex;align-items:center;justify-content:center;box-shadow:0 2px 10px rgba(0,0,0,.05)}
.node svg{width:34px;height:34px}
/* projects */
.proj-band{position:absolute;left:0;top:2623px;width:580px;height:230px;background:var(--ice)}
.dots{position:absolute;display:flex;gap:6px}
.dots i{display:block;height:3px;width:20px;background:#cfd8de}
.dots i.on{background:var(--teal);width:30px}
/* videos */
.play{position:absolute;left:50%;top:50%;width:34px;height:34px;margin:-17px 0 0 -17px;border-radius:50%;border:2px solid #fff;background:rgba(0,0,0,.35)}
.play::after{content:"";position:absolute;left:12px;top:9px;border-left:11px solid #fff;border-top:7px solid transparent;border-bottom:7px solid transparent}
/* testimonials */
.quote{position:absolute;width:260px;height:227px;background:var(--ice);padding:22px 18px}
.quote .mark{font-family:var(--serif);font-size:44px;line-height:34px;color:var(--teal);font-weight:700}
.quote p{font-size:10px;line-height:17.5px;color:#4c5660;margin-top:8px}
.who{display:flex;align-items:center;gap:10px;margin-top:12px}
.who span.av{width:22px;height:22px;border-radius:50%;background:#d7c4b8}
.who b{display:block;font-family:var(--serif);font-size:10px;color:var(--orange);font-weight:400}
.who small{font-size:9px;color:var(--muted)}
/* news */
.news{position:absolute;width:264px}
.news .date{font-size:9.5px;color:var(--orange)}
.news h4{font-family:var(--serif);font-size:11.5px;margin:6px 0}
.news p{font-size:9.5px;line-height:16px;color:var(--muted)}
/* contact */
.contact{position:absolute;left:0;top:4442px;width:1200px;height:328px;background:var(--ice-2)}
.field{position:absolute;background:#fff;border:1px solid #e1e7ec;font-size:9.5px;color:#9aa3ab;padding:10px 12px;height:32px}
/* footer */
.footer{position:absolute;left:0;top:4770px;width:1200px;height:282px;background:var(--footer);color:#fff}
.footer h5{font-family:var(--serif);font-size:12px;font-weight:700;margin-bottom:18px}
.footer ul{list-style:none;font-size:10px;line-height:21px;color:#d6dde6}
.contact-row{display:flex;gap:12px;align-items:flex-start;font-size:10px;line-height:16px;color:#d6dde6;margin-bottom:16px}
.contact-row svg{width:18px;height:18px;flex:none}
</style>
</head>
<body>

<!-- HERO -->
<header class="hero">
  <div class="hero-ship" role="img" aria-label="Cruise liner sailing at dusk on calm sea"></div>
  <nav class="nav">
    <span class="logo">VELTRO</span>
    <div class="menu"><span>MARINE</span><span>OUR BRANDS</span><span>ABOUT US</span><span>NEWS</span><span>CONTACT US</span></div>
    <span class="nav-cta">Contact Us</span>
  </nav>
  <h1>"Precision-Crafted Signage<br>To Enhance <em>Marine &amp;</em><br><em>Luxury Hotel</em> Spaces"</h1>
  <div class="btn" style="left:173px;top:340px;width:92px;height:31px;background:var(--navy)">Our Brand</div>
  <div class="brands"><span>Marivelle</span><span>Solvanta</span><span>Dunhaven Line</span><span>Tidemark</span><span>Lumen Cruises</span></div>
</header>

<!-- ABOUT -->
<section class="about-card">
  <h2>What If You Want To Go Your Own Way?</h2>
  <p class="body-text">At Veltro Design We Provide Comprehensive Signage Solutions For The Marine, Cruise, And Hospitality Industries, Combining Innovation With Precision. With Decades Of Experience, We Understand The Unique Demands Of Signage At Sea—From Regulatory Compliance To Durability In Harsh Marine Environments.<br>Our Dedicated Project Management Team Ensures That Each Project Is Completed Seamlessly From Initial Concept To Installation, Meeting All Specifications With Careful Attention To Every Detail. At Veltro Design We Provide Comprehensive Signage Solutions For The Marine, Cruise, And Hospitality Industries, Combining Innovation With Precision. With Decades Of Experience.</p>
  <div class="btn" style="left:31px;top:302px;width:98px;height:29px">Know More</div>
</section>
<div class="ph" style="left:537px;top:733px;width:489px;height:277px;background:linear-gradient(160deg,#3b3a36,#6c6152 50%,#2a2824)" role="img" aria-label="Hotel doorman at the entrance of the Wexbury Rowhouse Hotel"></div>

<!-- SERVICES -->
<h2 class="title abs" style="left:173px;top:1110px">Veltro - Services In Hospitality<br>And Marine Signage</h2>
<div class="btn" style="left:944px;top:1125px;width:82px;height:32px">View All</div>
<section class="svc-grid">
  <div class="svc"><svg viewBox="0 0 62 62" fill="none" stroke="#1c8db0" stroke-width="2"><rect x="10" y="12" width="42" height="30"/><path d="M18 36l9-10 7 7 5-5 7 8M22 50h18M31 42v8"/><circle cx="40" cy="20" r="3"/></svg><h3>Custom Signage Design</h3><p>Tailored Signage Solutions Crafted To Match Brand Identity And Aesthetic Preferences.</p></div>
  <div class="svc framed"><svg viewBox="0 0 62 62" fill="none" stroke="#1c8db0" stroke-width="2"><path d="M31 6v52M31 12h16l5 5-5 5H31M31 28H15l-5 5 5 5h16M22 58h18"/></svg><h3>Wayfinding And Navigation Systems</h3><p>Tailored Signage Solutions Crafted To Match Brand Identity And Aesthetic Preferences.</p></div>
  <div class="svc"><svg viewBox="0 0 62 62" fill="none" stroke="#1c8db0" stroke-width="2"><path d="M12 10l38 42M50 10L12 52M8 14l8-8M46 6l8 8M8 48l6 6M54 48l-6 6"/></svg><h3>Illuminated Signage</h3><p>Tailored Signage Solutions Crafted To Match Brand Identity And Aesthetic Preferences.</p></div>
  <div class="svc framed"><svg viewBox="0 0 62 62" fill="none" stroke="#1c8db0" stroke-width="2"><rect x="18" y="6" width="34" height="42"/><path d="M26 18h18M26 26h18M26 34h10M8 56h28M14 56v-8h16v8"/><path d="M38 38l4 4 8-8"/></svg><h3>Custom Signage Design</h3><p>Tailored Signage Solutions Crafted To Match Brand Identity And Aesthetic Preferences.</p></div>
  <div class="svc"><svg viewBox="0 0 62 62" fill="none" stroke="#1c8db0" stroke-width="2"><circle cx="31" cy="12" r="5"/><circle cx="12" cy="26" r="5"/><circle cx="50" cy="26" r="5"/><path d="M31 17v12M17 26h9M36 26h9M24 56V36a4 4 0 018 0v8h10a4 4 0 014 4v8"/></svg><h3>Regulatory And Safety Signage</h3><p>Tailored Signage Solutions Crafted To Match Brand Identity And Aesthetic Preferences.</p></div>
  <div class="svc framed"><svg viewBox="0 0 62 62" fill="none" stroke="#1c8db0" stroke-width="2"><path d="M14 8h34M20 8v10h22V8M26 18l5 16 5-16M31 34v8M12 56h38M18 56l4-10h18l4 10"/></svg><h3>Engraving And Etching</h3><p>Tailored Signage Solutions Crafted To Match Brand Identity And Aesthetic Preferences.</p></div>
</section>

<!-- HOW WE WORK -->
<div class="ph" style="left:285px;top:1697px;width:223px;height:283px;background:linear-gradient(180deg,#7b5e3c,#b98b55 50%,#4d3a26)" role="img" aria-label="Wooden cabin door with engraved room sign"></div>
<div class="ph" style="left:175px;top:1797px;width:147px;height:158px;background:linear-gradient(180deg,#8cb4d8,#e8edf0 60%,#2f4d6b)" role="img" aria-label="Cruise ship bow at port"></div>
<div class="ph" style="left:470px;top:1720px;width:117px;height:105px;background:linear-gradient(180deg,#1c3a6a,#3f78c0 60%,#12294d)" role="img" aria-label="Blue-lit theatre on board a cruise ship"></div>
<h2 class="title abs" style="left:619px;top:1669px">How We Work</h2>
<p class="body-text abs" style="left:619px;top:1708px;width:407px">Our Company Has 12 Years Of Experience In This Highly Specialized Field, And We Are Comprised Of A Highly Skilled Team Consisting Of Marine Engineers, Graphic Designers, Product Developers, Skilled Craftsman, Experienced Technicians And Installers. That Means We Have A Deep Understanding Of The Unique Challenges And Opportunities Of Our Constantly Evolving Industry—And The Skills, Systems, And Comprehensive Capabilities To Match It.</p>
<ul class="how-list">
  <li><svg viewBox="0 0 30 30" fill="none" stroke="#1c8db0" stroke-width="1.6"><circle cx="18" cy="8" r="4"/><path d="M3 22l6-4h8l4-3M3 26h18l6-6"/></svg>Customized Service For Cruise And Commercial Clients</li>
  <li><svg viewBox="0 0 30 30" fill="none" stroke="#1c8db0" stroke-width="1.6"><circle cx="15" cy="7" r="3"/><circle cx="7" cy="13" r="3"/><circle cx="23" cy="13" r="3"/><path d="M9 27v-6a6 6 0 0112 0v6M2 24a5 5 0 015-5M28 24a5 5 0 00-5-5"/></svg>Global Capabilities And The Teams To Make It Happen</li>
  <li><svg viewBox="0 0 30 30" fill="none" stroke="#1c8db0" stroke-width="1.6"><circle cx="15" cy="8" r="4"/><path d="M7 27v-6a8 8 0 0116 0v6M11 20l3 3 5-5"/></svg>Powered By A Culture Of "Yes"</li>
</ul>
<div class="btn" style="left:619px;top:1967px;width:98px;height:30px">Know More</div>

<!-- PROCESS -->
<section class="process">
  <h2 class="title" style="position:absolute;left:0;width:1200px;text-align:center;top:56px">Project Management</h2>
  <svg class="abs" style="left:0;top:0" width="1200" height="451" fill="none" stroke="#1c8db0" stroke-width="1.5" stroke-dasharray="4 4">
    <path d="M172 276H255M333 276H412M490 276H569M647 276H726M804 276H883M961 276H1026"/>
    <path d="M294 178V236M608 178V236M922 178V236M451 316V373M765 316V373" stroke-dasharray="3 3"/>
  </svg>
  <div class="node" style="left:255px;top:237px"><svg viewBox="0 0 34 34" fill="none" stroke="#d06e1f" stroke-width="1.6"><rect x="7" y="4" width="20" height="26"/><path d="M11 11h12M11 17h12M11 23h7"/></svg></div>
  <div class="node" style="left:412px;top:237px"><svg viewBox="0 0 34 34" fill="none" stroke="#d06e1f" stroke-width="1.6"><path d="M4 30h26M8 30V16h18v14M12 16V10h10v6M14 22h6"/></svg></div>
  <div class="node" style="left:569px;top:237px"><svg viewBox="0 0 34 34" fill="none" stroke="#d06e1f" stroke-width="1.6"><rect x="6" y="4" width="18" height="24"/><circle cx="20" cy="20" r="5"/><path d="M24 24l5 5M10 10h10"/></svg></div>
  <div class="node" style="left:726px;top:237px"><svg viewBox="0 0 34 34" fill="none" stroke="#d06e1f" stroke-width="1.6"><circle cx="17" cy="17" r="5"/><path d="M17 4v5M17 25v5M4 17h5M25 17h5M8 8l3.5 3.5M22.5 22.5L26 26M26 8l-3.5 3.5M11.5 22.5L8 26"/></svg></div>
  <div class="node" style="left:883px;top:237px"><svg viewBox="0 0 34 34" fill="none" stroke="#d06e1f" stroke-width="1.6"><rect x="6" y="4" width="20" height="26"/><path d="M10 12h12M10 18h6M17 24l9-9 3 3-9 9h-3z"/></svg></div>
  <div class="step" style="left:189px;top:113px"><h4>Initial Query</h4><p>Client Sends Query We Agree Specifications Of Their Requirements, Any Provided Artwork Handed Over.</p></div>
  <div class="step" style="left:503px;top:108px"><h4>Research</h4><p>Our Designers Research Requirements, Site Visits And Surveys Are Often Required.</p></div>
  <div class="step" style="left:817px;top:113px"><h4>Artwork Completed</h4><p>Artwork And Designs Are Completed By Our Designers Prior To Any Manufacture - We Always Seek Clients Approval.</p></div>
  <div class="step" style="left:331px;top:378px;width:240px"><h4>Manufacture</h4><p>If Offering Turnkey Solutions - We Will Have The Artwork Manufactured Through Specialist Signage Manufactures Across The Globe</p></div>
  <div class="step" style="left:645px;top:378px;width:240px"><h4>Install</h4><p>Our Project Management And Expert Install Team Have Traveled The Globe To Install Our Signs On Ships, Hotels And Other Venues.</p></div>
</section>

<!-- PROJECTS -->
<div class="proj-band"></div>
<div class="ph" style="left:173px;top:2645px;width:280px;height:185px;background:linear-gradient(160deg,#2a2f38,#4f5a6a 55%,#1d2128)" role="img" aria-label="Illuminated bistro sign in a ship lounge"></div>
<div class="ph" style="left:484px;top:2604px;width:276px;height:269px;background:linear-gradient(180deg,#9fb8cf,#e7edf1 35%,#1d3e7c 70%,#4c5a66)" role="img" aria-label="Cruise ship moored at the Varnoscali shipyard"></div>
<h2 class="title abs" style="left:792px;top:2642px">Our All Projects</h2>
<div class="abs" style="left:792px;top:2688px;font-family:var(--serif);font-size:11.5px;font-weight:700;color:var(--orange)">Varnoscali (Monfalcone, Italy)</div>
<p class="body-text abs" style="left:792px;top:2712px;width:234px">Client Sends Query We Agree Specifications Of Their Requirements, Any Provided Artwork Handed Over.</p>
<div class="dots" style="left:792px;top:2825px"><i class="on"></i><i></i><i></i><i></i></div>

<!-- VIDEOS -->
<h2 class="title abs" style="left:173px;top:2972px">We Have Worked</h2>
<div class="btn" style="left:944px;top:2973px;width:82px;height:32px">View All</div>
<div class="ph" style="left:173px;top:3038px;width:268px;height:149px;background:linear-gradient(160deg,#5a3c33,#a0473c 50%,#3b2a25)" role="img" aria-label="Classic car displayed in a hotel showroom"><span class="play"></span></div>
<div class="ph" style="left:465px;top:3038px;width:268px;height:149px;background:linear-gradient(170deg,#f1e7dc,#8a5a3b 60%,#d8c3ac)" role="img" aria-label="Hotel reception desk"><span class="play"></span></div>
<div class="ph" style="left:758px;top:3038px;width:268px;height:149px;background:linear-gradient(180deg,#6ea6d8,#dbe8f2 50%,#3e7fa9)" role="img" aria-label="Cruise ship at sea"><span class="play"></span></div>
<div class="ph" style="left:173px;top:3210px;width:414px;height:232px;background:linear-gradient(170deg,#1f6f99,#4aa0c5 50%,#0f4a72)" role="img" aria-label="Aerial view of a cruise ship sailing"><span class="play"></span></div>
<div class="ph" style="left:612px;top:3210px;width:414px;height:232px;background:linear-gradient(150deg,#35412d,#1d5a7a 45%,#63735a)" role="img" aria-label="Cruise ship navigating a narrow fjord"><span class="play"></span></div>

<!-- TESTIMONIALS -->
<h2 class="title abs" style="left:173px;top:3542px">What Clients Say</h2>
<div class="btn" style="left:944px;top:3544px;width:82px;height:32px">View All</div>
<div class="quote" style="left:173px;top:3636px"><div class="mark">“</div><p>Lorem Ipsum Dolor Sit Amet Consectetur. In Urna Et Risus Porttitor Id Lobortis Feugiat Eleifend Magna Fames Ullamcorper Tellus Non. Nisl Lacinia Purus Consequat Aenean Vitae Quis Cursus. Adipiscing Ultrices Libero Pretium Vel.</p><div class="who"><span class="av"></span><div><b>Marisa Holt</b><small>Customer</small></div></div></div>
<div class="quote" style="left:470px;top:3608px"><div class="mark">“</div><p>Lorem Ipsum Dolor Sit Amet Consectetur. In Urna Et Risus Porttitor Id Lobortis Feugiat Eleifend Magna Fames Ullamcorper Tellus Non. Nisl Lacinia Purus Consequat Aenean Vitae Quis Cursus. Adipiscing Ultrices Libero Pretium Vel.</p><div class="who"><span class="av"></span><div><b>Marisa Holt</b><small>Customer</small></div></div></div>
<div class="quote" style="left:767px;top:3636px"><div class="mark">“</div><p>Lorem Ipsum Dolor Sit Amet Consectetur. In Urna Et Risus Porttitor Id Lobortis Feugiat Eleifend Magna Fames Ullamcorper Tellus Non. Nisl Lacinia Purus Consequat Aenean Vitae Quis Cursus. Adipiscing Ultrices Libero Pretium Vel.</p><div class="who"><span class="av"></span><div><b>Marisa Holt</b><small>Customer</small></div></div></div>
<div class="dots" style="left:553px;top:3896px"><i class="on"></i><i></i><i></i><i></i></div>

<!-- NEWS -->
<h2 class="title abs" style="left:173px;top:3996px">Welcome To Our Hub For News,<br>Events And Recent Updates</h2>
<div class="btn" style="left:944px;top:4015px;width:82px;height:32px">View All</div>
<article class="news" style="left:173px;top:4093px">
  <div class="ph" style="position:relative;width:264px;height:174px;background:linear-gradient(170deg,#3b2a22,#7a4b35 55%,#1f1814)" role="img" aria-label="Hotel lobby doors"></div>
  <div class="date" style="margin-top:16px">Posted: 20 September, 2024</div><h4>Nordvik Line Unveil Nordvik Luna</h4><p>Lorem Ipsum Dolor Sit Amet Consectetur. Ut Nisl Enim Varius Justo Nunc Leo Nisi Nunc. Platea Pellentesque Turpis Pharetra Sit Sed......</p>
</article>
<article class="news" style="left:468px;top:4093px">
  <div class="date">Posted: 20 September, 2024</div><h4>Nordvik Line Unveil Nordvik Luna</h4><p>Lorem Ipsum Dolor Sit Amet Consectetur. Ut Nisl Enim Varius Justo Nunc Leo Nisi Nunc. Platea Pellentesque Turpis Pharetra Sit Sed......</p>
  <div class="ph" style="position:relative;margin-top:14px;width:264px;height:179px;background:linear-gradient(180deg,#cfd8e0,#f2f3f4 50%,#5a7ea8)" role="img" aria-label="Cruise ship hull at dry dock"></div>
</article>
<article class="news" style="left:762px;top:4093px">
  <div class="ph" style="position:relative;width:264px;height:174px;background:linear-gradient(170deg,#6f6a63,#2a2c30 60%,#8c8478)" role="img" aria-label="Townhouse hotel facade"></div>
  <div class="date" style="margin-top:16px">Posted: 20 September, 2024</div><h4>Nordvik Line Unveil Nordvik Luna</h4><p>Lorem Ipsum Dolor Sit Amet Consectetur. Ut Nisl Enim Varius Justo Nunc Leo Nisi Nunc. Platea Pellentesque Turpis Pharetra Sit Sed......</p>
</article>

<!-- CONTACT -->
<section class="contact">
  <div class="ph" style="left:173px;top:68px;width:482px;height:180px;background:radial-gradient(ellipse at 50% 50%,#2f7fd0 0%,#6eaee6 55%,rgba(243,248,251,0) 75%)" role="img" aria-label="World map with port locations marked"></div>
  <h2 class="title abs" style="left:708px;top:42px">Contact Us</h2>
  <div class="field" style="left:708px;top:88px;width:154px">Name</div>
  <div class="field" style="left:872px;top:88px;width:154px">Email</div>
  <div class="field" style="left:708px;top:133px;width:154px">Phone</div>
  <div class="field" style="left:872px;top:133px;width:154px">Subject</div>
  <div class="field" style="left:708px;top:178px;width:318px;height:58px">Message</div>
  <div class="btn" style="left:708px;top:248px;width:102px;height:32px">Submit Now</div>
</section>

<!-- FOOTER -->
<footer class="footer">
  <div class="abs" style="left:173px;top:60px;font-family:var(--serif);font-size:48px;letter-spacing:14px">VELTRO</div>
  <p class="abs" style="left:173px;top:140px;width:280px;font-size:9.5px;line-height:16px;color:#d6dde6">Lorem Ipsum Dolor Sit Amet Consectetur. Praesent Aliquam Massa Id Ornare Orci Eu. Maecenas Libero Enim Vulputate Viverra .......</p>
  <div class="abs" style="left:517px;top:52px"><h5>Quick Links</h5><ul><li>Challenges We Help</li><li>Services</li><li>Groups &amp; Courses</li><li>Our Team</li><li>Helpful Resources</li><li>Contact</li></ul></div>
  <div class="abs" style="left:698px;top:52px"><h5>Company</h5><ul><li>Careers</li><li>Locations</li><li>Downloads</li></ul></div>
  <div class="abs" style="left:837px;top:52px;width:200px"><h5>Get In Touch</h5>
    <div class="contact-row"><svg viewBox="0 0 18 18" fill="none" stroke="#fff" stroke-width="1.3"><circle cx="9" cy="9" r="8"/><path d="M9 4a3 3 0 013 3c0 2.5-3 6-3 6S6 9.5 6 7a3 3 0 013-3z"/></svg>Suite 4, 28 Calder Row,<br>London EC2A 4LT</div>
    <div class="contact-row"><svg viewBox="0 0 18 18" fill="none" stroke="#fff" stroke-width="1.3"><circle cx="9" cy="9" r="8"/><path d="M6 5l2 2-1 1.5a6 6 0 003 3L11.5 10l2 2-1.5 1.5C9 13 5 9 4.5 5.5z"/></svg>020 7946 0382</div>
    <div class="contact-row"><svg viewBox="0 0 18 18" fill="none" stroke="#fff" stroke-width="1.3"><circle cx="9" cy="9" r="8"/><rect x="4.5" y="6" width="9" height="6"/><path d="M4.5 6l4.5 3.5L13.5 6"/></svg>info@veltrosigns.example</div>
  </div>
  <div class="abs" style="left:173px;top:250px;font-size:9px;color:#c5cfd9">© 2024 Veltro. All Rights Reserved</div>
  <div class="abs" style="left:557px;top:250px;font-size:9px;color:#c5cfd9;display:flex;gap:30px"><span>Site Notice</span><span>Privacy Policy</span><span>Terms</span></div>
  <div class="abs" style="left:940px;top:249px;font-size:9px;font-weight:600;display:flex;gap:16px"><span>Social</span><span>Network</span></div>
</footer>

</body>
</html>
```